Hi Marivonne, we need our wine labels produced for this year's vintage with a few changes. We would like to keep the integrity of the current label for the H and want the blue and gold to remain in the design. However we would like to include an image of a tree and our dogs.

```html
<!DOCTYPE html>
<html lang="en">
<head>
<meta charset="utf-8">
<title>Corvane Estate — Pinot Noir 2016 Label</title>
<link rel="stylesheet" href="https://fonts.googleapis.com/css2?family=Marcellus&family=Josefin+Sans:wght@600&display=swap">
<style>
  :root {
    --backdrop: #e4d5b4;
    --navy: #1c1d5c;
    --navy-deep: #15164a;
    --ink-blue: #2b2a8c;
    --cream: #e0cfb8;
    --gold: #d2a464;
    --shadow: rgba(40, 30, 20, 0.35);
  }
  * { box-sizing: border-box; margin: 0; padding: 0; }
  html, body {
    width: 1200px;
    height: 900px;
    overflow: hidden;
    background: var(--backdrop);
  }
  .canvas {
    position: relative;
    width: 1200px;
    height: 900px;
    display: flex;
    align-items: center;
    justify-content: center;
  }
  .label {
    position: relative;
    width: 474px;
    height: 820px;
    background: radial-gradient(ellipse at 50% 20%, #22246a 0%, var(--navy) 55%, var(--navy-deep) 100%);
    box-shadow: 14px 16px 22px var(--shadow);
  }
  .label-panel {
    position: absolute;
    left: 66px;
    top: 74px;
    width: 342px;
    height: 658px;
    background: var(--cream);
    padding: 6px;
  }
  .gold-frame {
    width: 100%;
    height: 100%;
    border: 6px solid var(--gold);
    padding: 6px;
  }
  .inner-frame {
    position: relative;
    width: 100%;
    height: 100%;
    border: 1px solid var(--ink-blue);
    text-align: center;
    color: var(--ink-blue);
  }
  .estate-name {
    margin-top: 24px;
    font-family: "Marcellus", serif;
    font-weight: 400;
    font-size: 50px;
    line-height: 48px;
    letter-spacing: 4px;
  }
  .estate-name span { display: block; }
  .varietal {
    margin-top: 20px;
    font-family: "Josefin Sans", sans-serif;
    font-weight: 600;
    font-size: 16px;
    line-height: 20px;
    letter-spacing: 2.5px;
  }
  .artwork {
    position: absolute;
    left: 22px;
    top: 186px;
    width: 266px;
    height: 418px;
    background: linear-gradient(180deg, rgba(43, 42, 140, 0.55) 0%, var(--ink-blue) 70%, rgba(43, 42, 140, 0.8) 100%);
  }
</style>
</head>
<body>
  <main class="canvas">
    <section class="label" aria-label="Corvane Estate Pinot Noir 2016 wine label">
      <div class="label-panel">
        <div class="gold-frame">
          <div class="inner-frame">
            <h1 class="estate-name"><span>CORVANE</span><span>ESTATE</span></h1>
            <p class="varietal">PINOT NOIR<br>2016</p>
            <div class="artwork" role="img" aria-label="Blue silhouette of a tall fir tree on a grassy knoll with two small terriers standing beneath it"></div>
          </div>
        </div>
      </div>
    </section>
  </main>
</body>
</html>
```